Company brochure for our unique consulting business

We are a small consulting business offering a unique set of services to our clients.. In simple terms we are a business improvement consultancy helping our clients get the best out of their businesses. We work with clients across multiple sectors and deliver a variety of services. We want to put together a brochure to cover these main themes:1. Who we are2. What we do3. The type of people we employ4. The sectors we work inWhile the brochure needs to have a certain corporate feel to it, we don't want it to be "boring" or "stiff". We would like it to have a slightly "friendly" or "informal" feel to it, to reflect the type of organisation we are.We have a company website http://tollandvergeadvisory.com , however we do not want to directly replicate the content or feel as we recognise it needs updating.We would like the brochure to be A4 portrait format. We anticipate requiring 12 sides (including covers) but we are happy to be guided on this based on the content we have provided.The attached ppt file gives the detail of the content to be included and also shows the proposed pagination. For the front cover we would like to try 2 versions, one with the TVA logo and one with the Tolland Verge Advisory logo (a file of both is attached)One of the most important pages will be the "Our Services" page. We would like this to cover the centre fold. In the ppt file we have shown an example layout, but this is where we need most help - we are clearly not graphic designers! This page will be the most used page in sales meetings etc.Also attached is the following:1. file for our TollandVerge Advisory company logo.2. File for our TVA company logo3. Files for Derek's signatures (for under photos) - Owen's to follow4. Photo of Derek & Owen (person in purple shirt to be cropped out)Thank you and really excited to see what everyone comes back with.Derek & Owen

Target Market(s)

Very broad - Manufacturing, Healthcare, Hospitality

Industry/Entity Type

Management Consulting

Font styles to use
Other font styles liked:
• We use Swiss721, but happy to be guided by designer

Colors
3276b5
85abd2
0355a3
333333
5c5c5c
9d9d9d
d9d9d9

Requirements
Must have
• Corporate feel
Nice to have
• Slightly friendly feel
• Our standard "blue" is (CORRECTION) - R55 G96 B146 #376092 and our standard grey is R197 G178, B179 - #B3B2B2, which we would like to keep, but other colours we are happy to be guided on. Brand guidelines attached.

```html
<!DOCTYPE html>
<html lang="en">
<head>
<meta charset="utf-8">
<title>Tolland Verge Advisory — Values and Regions Spread</title>
<link rel="stylesheet" href="https://fonts.googleapis.com/css2?family=Roboto:wght@300;400;700&display=swap">
<style>
  :root {
    --backdrop: #e4e4e4;
    --paper: #f4f4f4;
    --paper-shade: #ebebeb;
    --brand-blue: #0b4ea2;
    --brand-blue-deep: #0355a3;
    --ink: #333333;
    --ink-soft: #5c5c5c;
    --rule: #9d9d9d;
    --white: #ffffff;
  }
  * { box-sizing: border-box; margin: 0; padding: 0; }
  html, body {
    width: 1200px; height: 840px; overflow: hidden;
    background: var(--backdrop);
    font-family: "Roboto", Arial, sans-serif;
    color: var(--ink);
  }
  .spread {
    position: absolute; left: 50px; top: 30px;
    width: 1100px; height: 780px;
    display: flex;
    box-shadow: 0 10px 30px rgba(0,0,0,0.18);
  }
  .page { position: relative; width: 550px; height: 780px; overflow: hidden; }

  /* Left page */
  .page--values { background: #6d6d6d; }
  .building-photo {
    position: absolute; inset: 0;
    background: linear-gradient(160deg, #d9d9d9 0%, #9a9a9a 35%, #4a4a4a 70%, #2a2a2a 100%);
  }
  .values-panel {
    position: absolute; left: 120px; top: 60px;
    width: 240px; height: 450px;
    background: var(--brand-blue);
    padding: 26px 22px;
    color: var(--white);
  }
  .section-title {
    display: inline-flex; align-items: stretch;
    font-size: 11px; font-weight: 700; letter-spacing: 1px;
    text-transform: uppercase; margin-bottom: 22px;
  }
  .section-title__lead {
    padding: 2px 5px 2px 4px;
    border-left: 2px solid currentColor;
    border-top: 1px solid currentColor;
    border-bottom: 1px solid currentColor;
  }
  .section-title__tag { padding: 3px 6px; background: var(--white); color: var(--brand-blue); }
  .values-list { list-style: none; }
  .values-list li {
    position: relative; padding-left: 16px; margin-bottom: 18px;
    font-size: 11px; line-height: 1.5; font-weight: 300;
  }
  .values-list li::before {
    content: ""; position: absolute; left: 0; top: 5px;
    border-left: 6px solid var(--white);
    border-top: 4px solid transparent; border-bottom: 4px solid transparent;
  }
  .brand-name {
    position: absolute; left: 40px; bottom: 40px;
    display: flex; align-items: center; gap: 8px;
    color: var(--white); font-size: 20px; font-weight: 700; letter-spacing: 1px;
  }
  .brand-name__mark { width: 10px; height: 10px; background: var(--white); }

  /* Right page */
  .page--regions {
    background: linear-gradient(90deg, var(--paper-shade) 0%, var(--paper) 8%, var(--paper) 100%);
  }
  .team-photo {
    position: absolute; left: 100px; top: 60px;
    width: 290px; height: 200px;
    background: linear-gradient(135deg, #cfcfcf, #8e8e8e);
  }
  .values-note {
    position: absolute; left: 408px; top: 90px; width: 118px;
    color: var(--ink-soft);
  }
  .values-note .section-title { color: var(--brand-blue); margin-bottom: 12px; font-size: 10px; }
  .values-note .section-title__tag { background: var(--brand-blue); color: var(--white); }
  .values-note p { font-size: 9px; line-height: 1.55; }
  .edge-bar {
    position: absolute; right: 0; top: 90px;
    width: 18px; height: 250px; background: var(--brand-blue);
  }
  .signatures {
    position: absolute; left: 70px; top: 272px;
    width: 300px; height: 46px;
    background: linear-gradient(90deg, #dcdcdc, #c4c4c4);
  }
  .intro-text {
    position: absolute; left: 70px; top: 330px; width: 380px;
    font-size: 10px; line-height: 1.55; color: var(--ink-soft);
  }
  .regions-block { position: absolute; left: 60px; top: 410px; width: 380px; }
  .regions-block .section-title { color: var(--brand-blue); font-size: 10px; margin-bottom: 10px; }
  .regions-block .section-title__tag { background: var(--brand-blue); color: var(--white); }
  .world-map {
    width: 360px; height: 190px;
    background: linear-gradient(160deg, #2f6fb8, #0b4ea2);
    border-radius: 4px;
  }
  .page-rule {
    position: absolute; left: 60px; right: 40px; top: 700px;
    height: 1px; background: var(--rule);
  }
  .page-foot {
    position: absolute; right: 40px; bottom: 30px;
    display: flex; align-items: center; gap: 8px;
    font-size: 9px; color: var(--ink-soft);
  }
</style>
</head>
<body>
  <main class="spread">
    <section class="page page--values">
      <div class="building-photo" role="img" aria-label="Black and white photograph of a modern glass office building"></div>
      <div class="values-panel">
        <h2 class="section-title"><span class="section-title__lead">Our</span><span class="section-title__tag">Values</span></h2>
        <ul class="values-list">
          <li>We deliver lasting value by listening first and acting with care.</li>
          <li>We build honest partnerships grounded in trust and plain speaking.</li>
          <li>We measure success by the results our clients achieve.</li>
          <li>We develop practical solutions that fit each business.</li>
          <li>We share what we know so teams keep improving.</li>
          <li>We take personal responsibility for every promise we make.</li>
        </ul>
      </div>
      <div class="brand-name"><span class="brand-name__mark"></span>TVA</div>
    </section>

    <section class="page page--regions">
      <div class="team-photo" role="img" aria-label="Photograph of the two founders, Derek and Owen, at work"></div>
      <aside class="values-note">
        <h3 class="section-title"><span class="section-title__lead">Our</span><span class="section-title__tag">Values</span></h3>
        <p>At our core we commit to deliver the best possible value for every client, working side by side as one team.</p>
      </aside>
      <div class="edge-bar"></div>
      <div class="signatures" role="img" aria-label="Handwritten signatures of Derek and Owen"></div>
      <p class="intro-text">Bringing together our expertise from industry and our experience of working with multiple organisations to help our clients deliver results against their own business goals.</p>
      <div class="regions-block">
        <h3 class="section-title"><span class="section-title__lead">Our</span><span class="section-title__tag">Regions</span></h3>
        <div class="world-map" role="img" aria-label="World map in blue with callouts marking the regions where the firm works"></div>
      </div>
      <div class="page-rule"></div>
      <div class="page-foot">
        <svg width="22" height="12" viewBox="0 0 22 12" aria-hidden="true">
          <g fill="#0b4ea2">
            <rect x="0" y="0" width="3" height="12"/><rect x="6" y="0" width="3" height="12"/>
            <rect x="12" y="0" width="3" height="12"/><rect x="18" y="0" width="3" height="12"/>
          </g>
        </svg>
        <span>3</span>
      </div>
    </section>
  </main>
</body>
</html>
```